Laundry Service Description Tri-Fold Brochure

My laundry business offers a service called "Mellowtide - Wet Cleaning"
I am after a design for a tri fold brochure to hand out to my customers. This will detail the benefits of wet cleaning vs dry cleaning.
I want the brochure to highlight the customer benefits NOT the business benefits.
I have attached the logo of our laundry which should be included
A couple of links here for more information and pdfs are attached:
https://brimleyhollandsupply.com.au/laundry/mellow-tide-wet-cleaning.html
https://www.quorv.co.za/wet-cleaning/
I have attached the design of our laundry window and ideally i want the brochure designed similar

```html
<!DOCTYPE html>
<html lang="en">
<head>
<meta charset="utf-8">
<title>Harborline Laundry Services – Tri-Fold Brochure</title>
<link href="https://fonts.googleapis.com/css2?family=Montserrat:wght@500;600&family=Open+Sans:wght@400;600&family=Comfortaa:wght@600&display=swap" rel="stylesheet">
<style>
:root{
  --page:#e6e7ea;
  --navy:#0a3f86;
  --blue:#1670c4;
  --sky:#3ea6e6;
  --pale:#bfe3f8;
  --ice:#e8f5fd;
  --white:#ffffff;
  --ink:#3c4650;
  --accent:#1c7fcf;
}
*{box-sizing:border-box;margin:0;padding:0}
html,body{width:770px;height:1200px;overflow:hidden;background:var(--page)}
body{position:relative;font-family:"Open Sans",Arial,sans-serif;color:var(--white)}
.sheet{position:absolute;left:45px;width:683px;height:531px;overflow:hidden;box-shadow:0 8px 14px rgba(0,0,0,.22);background:var(--white)}
.sheet--outside{top:40px}
.sheet--inside{top:632px}
.panel{position:absolute;top:0;height:100%;overflow:hidden}
.photo{position:absolute;background:radial-gradient(circle at 45% 40%,#d9eefa,#7fc2ec 70%,#4a9fdc);}
.bubble{position:absolute;border-radius:50%;background:var(--white);box-shadow:inset -1px -1px 3px rgba(30,110,190,.35)}
.bubble--blue{background:var(--pale);box-shadow:none}
.heading{font-family:"Montserrat",Arial,sans-serif;font-weight:500;letter-spacing:.5px}
.body-text{font-size:6.9px;line-height:1.48;text-align:justify}
.body-text p+p{margin-top:8px}
.pill{position:absolute;height:21px;border-radius:11px;background:linear-gradient(#d6eefc,#a9d9f6);color:var(--navy);font-size:9.5px;display:flex;align-items:center;justify-content:center;letter-spacing:.2px}
.brand{position:absolute;display:flex;align-items:center;gap:6px;font-family:"Comfortaa",Arial,sans-serif;font-weight:600}
.brand__dot{width:9px;height:9px;border-radius:50%;border:2px solid currentColor}
.tagline{position:absolute;left:0;right:0;text-align:center;font-family:"Montserrat",Arial,sans-serif}

/* outside: about panel */
.about{left:0;width:228px;background:linear-gradient(180deg,#4fb0ea 0%,#1a74c6 45%,#0b4691 100%)}
.about__photo{left:-30px;top:-40px;width:265px;height:205px;border-radius:0 0 50% 50%/0 0 45% 45%;border-bottom:6px solid var(--pale)}
.about__title{position:absolute;left:15px;top:186px;font-size:12px}
.about__text{position:absolute;left:15px;top:210px;width:200px}

/* outside: contact panel */
.contact{left:228px;width:227px;background:linear-gradient(180deg,#fff 0%,#f3f9fe 100%);color:var(--ink)}
.contact__ring{position:absolute;left:38px;top:84px;width:120px;height:120px;border-radius:50%;background:var(--white);border:6px solid var(--blue)}
.contact__photo{left:45px;top:91px;width:106px;height:106px;border-radius:50%}
.contact .brand{left:0;right:0;top:270px;justify-content:center;color:var(--blue);font-size:24px}
.contact .tagline--main{top:313px;font-size:11px;color:var(--accent);font-weight:500}
.contact .tagline--sub{top:327px;font-size:9.5px;color:var(--sky)}
.contact__text{position:absolute;left:12px;top:351px;width:203px;font-size:6.4px;line-height:1.5;text-align:center;color:var(--ink)}
.contact__cta{position:absolute;left:0;right:0;top:429px;text-align:center;font-size:9px;color:var(--accent);font-weight:600}
.contact .pill{left:30px;top:446px;width:167px;height:24px;border-radius:12px;font-size:14px;color:var(--accent)}
.contact__web{position:absolute;left:0;right:0;top:478px;text-align:center;font-size:9px;color:var(--accent);font-weight:600}

/* outside: cover panel */
.cover{left:455px;width:228px;background:linear-gradient(180deg,#eaf6fd 0%,#3c9de0 55%,#0b4691 100%)}
.cover__photo{left:-55px;top:-30px;width:300px;height:330px;border-radius:50%;border-bottom:10px solid var(--sky)}
.cover .brand{left:0;right:0;top:370px;justify-content:center;color:var(--white);font-size:27px}
.cover .tagline--main{top:437px;font-size:11.5px;font-weight:500}
.cover .tagline--sub{top:460px;font-size:10px;color:var(--pale)}

/* inside */
.benefits{left:0;width:468px;background:linear-gradient(180deg,#2f95dc 0%,#1466b8 55%,#0b4691 100%)}
.benefits__wave{position:absolute;left:0;top:0}
.benefits__title{position:absolute;top:70px;font-size:11.5px}
.vs{position:absolute;left:213px;top:64px;width:26px;height:26px;border-radius:50%;background:var(--pale);color:var(--blue);font-size:9px;display:flex;align-items:center;justify-content:center;font-family:"Montserrat",Arial,sans-serif}
.column{position:absolute;top:94px;width:200px}
.column--wet{left:15px}
.column--dry{left:230px;width:208px}
.bullets{list-style:none;margin-top:10px;font-size:6.9px;line-height:1.5}
.bullets li{padding-left:7px;text-indent:-7px;margin-bottom:1.5px}
.bullets li::before{content:"• "}
.benefits__photo{left:0;top:378px;width:290px;height:190px;border-radius:0 60% 0 0/0 80% 0 0}
.benefits__shirts{left:250px;top:370px;width:96px;height:96px;border-radius:50%;border:5px solid var(--white)}
.benefits .brand{left:296px;top:470px;color:var(--white);font-size:24px}
.benefits__web{position:absolute;left:296px;top:506px;font-size:8.5px;color:var(--pale)}

.compare{left:468px;width:215px;background:var(--white)}
.compare__photo{left:-10px;top:-20px;width:235px;height:200px;border-radius:0 0 50% 50%/0 0 55% 55%;border-bottom:6px solid var(--sky)}
.compare__grid{position:absolute;left:10px;top:228px;width:198px;height:283px;display:grid;grid-template-columns:1fr 1fr;gap:0 4px}
.compare__col{background:var(--pale);color:var(--blue);text-align:center;padding-top:40px}
.compare__badge{position:absolute;top:-15px;width:50px;height:50px;border-radius:50%;background:var(--accent);border:3px solid var(--white);display:flex;align-items:center;justify-content:center}
.compare__badge--wet{left:24px}
.compare__badge--dry{left:126px}
.compare__vs{position:absolute;left:91px;top:0;width:16px;height:16px;border-radius:50%;background:var(--accent);color:var(--white);font-size:5.5px;display:flex;align-items:center;justify-content:center;border:1.5px solid var(--white)}
.compare__head{font-size:8px;font-family:"Montserrat",Arial,sans-serif;font-weight:500;padding-bottom:4px;border-bottom:1px solid var(--white)}
.cell{height:56px;padding:5px 6px 0;border-bottom:1px solid var(--white)}
.cell:last-child{border-bottom:0}
.cell svg{display:block;margin:0 auto 3px}
.cell b{display:block;font-size:4.8px;font-weight:600}
.cell span{display:block;font-size:4.6px;line-height:1.35;color:#2d6aa8}
</style>
</head>
<body>

<section class="sheet sheet--outside">
  <article class="panel about">
    <div class="photo about__photo" role="img" aria-label="Smiling woman holding a stack of freshly folded laundry"></div>
    <span class="bubble" style="left:183px;top:12px;width:13px;height:13px"></span>
    <span class="bubble" style="left:203px;top:32px;width:9px;height:9px"></span>
    <span class="bubble" style="left:210px;top:62px;width:10px;height:10px"></span>
    <span class="bubble" style="left:175px;top:46px;width:7px;height:7px"></span>
    <span class="bubble bubble--blue" style="left:186px;top:140px;width:28px;height:28px;opacity:.7"></span>
    <h2 class="heading about__title">ABOUT US</h2>
    <div class="body-text about__text">
      <p>Harborline Laundry is a professional laundry service provider covering Protaras and surrounding areas and is committed to delivering the top quality laundry, wet cleaning and ironing service in Cyprus. Harborline Laundry provides all laundry facilities, including dry cleaning, wash and iron, washing clothes, ironing and laundry collection and delivery within 24 hours.</p>
      <p>We offer on demand services like laundry, wet cleaning, ironing, wedding dress cleaning, clothing alterations, commercial laundry and commercial wet cleaning with free pickup and delivery at your doorstep on time. We use high-tech washing machines and the use of biodegradable and eco-friendly laundry detergents.</p>
      <p>In just 24 hours, our drivers will pick up all of your dirty laundry and deliver it cleaned and folded. We are the best dry cleaning and laundry service on the East Coast of Cyprus because of our unmatched, undivided attention to minor information, expert wet cleaners team and loyalty to our clients. Our keen attention to the smallest details, such as removing stubborn stains from your garments before washing them further, or treating fragile fabrics with the utmost respect, has distinguished us as a one of a kind laundry collection in Cyprus.</p>
    </div>
    <div class="pill" style="left:15px;top:497px;width:200px">www.harborlinelaundry.com.cy</div>
  </article>

  <article class="panel contact">
    <span class="bubble bubble--blue" style="left:28px;top:178px;width:34px;height:34px"></span>
    <div class="contact__ring"></div>
    <div class="photo contact__photo" role="img" aria-label="Stack of folded striped and blue shirts"></div>
    <span class="bubble" style="left:20px;top:290px;width:11px;height:11px;background:var(--sky)"></span>
    <span class="bubble" style="left:16px;top:306px;width:6px;height:6px;background:var(--sky)"></span>
    <div class="brand"><span class="brand__dot"></span>Harborline</div>
    <p class="tagline tagline--main">MELLOWTIDE • WET CLEANING</p>
    <p class="tagline tagline--sub">We are passionate about laundry!</p>
    <p class="contact__text">We are professionals in the laundry and dry cleaning business, which means we always stay up to date on the latest technologies, cleaning methods, and solutions for dealing with stains or delicate fabrics. Plus, we maintain the highest standards of business integrity by following local and national regulations and environmental safety rules.</p>
    <p class="contact__cta">CONTACT US TODAY!</p>
    <div class="pill">+357 24 610 388</div>
    <p class="contact__web">www.harborlinelaundry.com.cy</p>
    <span class="bubble bubble--blue" style="left:195px;top:468px;width:14px;height:14px"></span>
    <span class="bubble bubble--blue" style="left:186px;top:490px;width:8px;height:8px"></span>
    <span class="bubble bubble--blue" style="left:202px;top:502px;width:6px;height:6px"></span>
  </article>

  <article class="panel cover">
    <div class="photo cover__photo" role="img" aria-label="Bearded man in an apron holding a pile of laundry and giving an OK sign"></div>
    <span class="bubble" style="left:0px;top:30px;width:18px;height:18px"></span>
    <span class="bubble" style="left:18px;top:60px;width:10px;height:10px"></span>
    <span class="bubble" style="left:0px;top:78px;width:8px;height:8px"></span>
    <div class="brand"><span class="brand__dot"></span>Harborline</div>
    <p class="tagline tagline--main">MELLOWTIDE • WET CLEANING</p>
    <p class="tagline tagline--sub">We are passionate about laundry!</p>
    <div class="pill" style="left:15px;top:497px;width:200px">www.harborlinelaundry.com.cy</div>
  </article>
</section>

<section class="sheet sheet--inside">
  <article class="panel benefits">
    <svg class="benefits__wave" width="468" height="60" viewBox="0 0 468 60" aria-hidden="true">
      <path d="M0 0H468V14C360 28 180 34 0 46Z" fill="#bfe3f8"/>
      <path d="M0 0H468V4C360 14 180 20 0 28Z" fill="#ffffff"/>
    </svg>
    <h2 class="heading benefits__title" style="left:15px">BENEFITS OF WET CLEANING</h2>
    <div class="vs">VS</div>
    <h2 class="heading benefits__title" style="left:248px">DRY CLEANING</h2>

    <div class="column column--wet">
      <p class="body-text">A better clean, in a better way. Our machines have been adapted to achieve fourth generation wet cleaning capability. This means that the equipment we use is able to process both wet and dry clean-only items as well as standard laundry. Our process therefore results in a huge increase in efficiency and quality and you get items back cleaner, faster and with significantly less impact on the environment.</p>
      <ul class="bullets">
        <li>A superior natural way of cleaning fabrics</li>
        <li>No harsh chemicals such as chlorine or phosphates are used protecting both your garments and you</li>
        <li>Uses water and mild biodegradable detergents instead of polluting chemicals such as PERC, so no toxic waste is produced</li>
        <li>Leaves a fresh natural scent instead of a chemical</li>
        <li>Removes organic stains better than dry cleaning</li>
        <li>Turn around time is half that of dry cleaning</li>
        <li>There are minimal epidermal issues and the process is hypoallergenic and more suitable for sensitive skin</li>
        <li>Gentle drum rotation with water showering means less felting, matting, friction and overall material damage</li>
      </ul>
    </div>

    <div class="column column--dry">
      <p class="body-text">Dry cleaning is cleaning process for clothing and textiles using a solvent other than water. Dry cleaning still involves liquid, but clothes are instead soaked in a water-free liquid solvent. Dry cleaning causes many health issues ranging from respiratory failure to cancer. It can also have adverse effects on the human nervous system, causing headaches, movement difficulties and memory loss.</p>
      <ul class="bullets">
        <li>Protects brightness and color of your garments</li>
        <li>Dissolves grease and oil stains better than water-based cleaning methods like wet cleaning.</li>
        <li>Preserves natural fibers such as silk and wool</li>
        <li>Retains your garments' original texture, finish and sheen</li>
        <li>Dry Cleaning Preserves Delicate Fabrics</li>
        <li>Professional dry cleaners pay close attention to detail</li>
        <li>Dry cleaning is perfect for stain and odor removal</li>
        <li>Dry cleaners can handle large items</li>
        <li>Dry cleaning helps your clothing to last longer</li>
      </ul>
    </div>

    <div class="photo benefits__photo" role="img" aria-label="Two laundry staff holding a folded white towel beside a washing machine"></div>
    <div class="photo benefits__shirts" role="img" aria-label="Stack of folded colourful shirts"></div>
    <span class="bubble" style="left:232px;top:352px;width:16px;height:16px"></span>
    <span class="bubble" style="left:222px;top:372px;width:8px;height:8px"></span>
    <div class="brand"><span class="brand__dot"></span>Harborline</div>
    <p class="benefits__web">www.harborlinelaundry.com.cy</p>
  </article>

  <article class="panel compare">
    <div class="photo compare__photo" role="img" aria-label="Smiling laundry attendant handing a ticket to a customer at the counter"></div>
    <span class="bubble bubble--blue" style="left:12px;top:160px;width:20px;height:20px"></span>
    <div class="compare__grid">
      <div class="compare__badge compare__badge--wet">
        <svg width="22" height="22" viewBox="0 0 22 22" aria-hidden="true"><path d="M8 3C5 8 3 11 3 14a5 5 0 0 0 10 0c0-3-2-6-5-11Z M15 6c-2 3-3 5-3 6.5a3 3 0 0 0 6 0C18 11 17 9 15 6Z" fill="none" stroke="#fff" stroke-width="1.3"/></svg>
      </div>
      <div class="compare__vs">VS</div>
      <div class="compare__badge compare__badge--dry">
        <svg width="22" height="22" viewBox="0 0 22 22" aria-hidden="true"><path d="M5 4h12v15H5Z M8 4l3 4 3-4 M11 8v11" fill="none" stroke="#fff" stroke-width="1.3"/></svg>
      </div>

      <div class="compare__col">
        <p class="compare__head">WET CLEANING</p>
        <div class="cell"><svg width="12" height="14" viewBox="0 0 12 14"><path d="M6 1C3 5 2 7 2 9a4 4 0 0 0 8 0c0-2-1-4-4-8Z" fill="none" stroke="#1c7fcf"/></svg><b>USES WATER</b><span>Uses water, detergents, soaps and bleaches, rather than chemical solvents</span></div>
        <div class="cell"><svg width="12" height="14" viewBox="0 0 12 14"><path d="M2 12L10 2M4 12c4 0 6-4 6-10C5 3 3 7 4 12Z" fill="none" stroke="#1c7fcf"/></svg><b>GENTLER ON FABRICS</b><span>Water is gentler than solvents on fabrics and can extend a garment's life.</span></div>
        <div class="cell"><svg width="14" height="14" viewBox="0 0 14 14"><path d="M1 5h12l-2 7H3Z M4 5V2h6v3" fill="none" stroke="#1c7fcf"/></svg><b>BETTER ON ORGANIC STAINS</b><span>Removes tough organic stains like sweat, mildew, etc better than dry cleaning</span></div>
        <div class="cell"><svg width="22" height="14" viewBox="0 0 22 14"><path d="M1 3l3-2h2l1 1 1-1h2l3 2-2 2-1-1v9H3V4L2 5Z" fill="none" stroke="#1c7fcf"/><path d="M15 8h4m-1-1 1 1-1 1" stroke="#1c7fcf" fill="none"/></svg><b>CAN DISTORT GARMENTS</b><span>Clothes may shrink or stretch when saturated with water during wet cleaning</span></div>
      </div>

      <div class="compare__col">
        <p class="compare__head">DRY CLEANING</p>
        <div class="cell"><svg width="10" height="14" viewBox="0 0 10 14"><path d="M3 1h4v2H3Z M2 3h6v10H2Z" fill="none" stroke="#1c7fcf"/></svg><b>USES A LIQUID SOLVENT</b><span>Uses environmentally-friendly chemical solvents rather than water.</span></div>
        <div class="cell"><svg width="14" height="14" viewBox="0 0 14 14"><path d="M4 2h6l3 3-2 1v7H3V6L1 5Z" fill="none" stroke="#1c7fcf"/></svg><b>PROTECTS COLORS</b><span>Preserves the brightness, color and original sheen of your garments unlike water</span></div>
        <div class="cell"><svg width="12" height="14" viewBox="0 0 12 14"><path d="M2 1h8v12H2Z M6 5c-1 2-2 3-2 4a2 2 0 0 0 4 0c0-1-1-2-2-4Z" fill="none" stroke="#1c7fcf"/></svg><b>BETTER ON OIL-BASED STAIN</b><span>Dissolves grease and oil-based stains better than wet cleaning</span></div>
        <div class="cell"><svg width="12" height="14" viewBox="0 0 12 14"><path d="M4 1h4 M5 1v4L1 13h10L7 5V1" fill="none" stroke="#1c7fcf"/></svg><b>NOT BIODEGRADIVE</b><span>Less environmentally-friendly than water used in wet cleaning</span></div>
      </div>
    </div>
  </article>
</section>

</body>
</html>
```